Napa Winery - Chardonnay wine label

We are looking for a label for a new Napa Valley winery - chardonnay wine. The winery is "Harrowgate Ridge Vintners" and we would like to see it depicted on a white wine (chardonnay style) bottle. The winery is called Harrowgate Ridge Vintners.

We are open to ideas!

Target Market(s)

High-end chardonnay lovers

Requirements
Nice to have
• Painted or etched label onto bottle

```html
<!DOCTYPE html>
<html lang="en">
<head>
<meta charset="utf-8">
<title>Harrowgate Ridge Vintners – Chardonnay Label</title>
<link rel="stylesheet" href="https://fonts.googleapis.com/css2?family=EB+Garamond:wght@400;600&display=swap">
<style>
  :root {
    --page-bg: #fdfdfb;
    --label-paper: #f5f4f4;
    --frame-gold: #d9d2b8;
    --ink: #262424;
    --body-grey: #9a9898;
    --accent-gold: #a88c3c;
    --art-light: #e4e2de;
    --art-dark: #8a8784;
  }
  * { margin: 0; padding: 0; box-sizing: border-box; }
  html, body {
    width: 1200px;
    height: 1104px;
    overflow: hidden;
    background: var(--page-bg);
  }
  .canvas {
    position: relative;
    width: 1200px;
    height: 1104px;
  }
  .wine-label {
    position: absolute;
    left: 150px;
    top: 124px;
    width: 900px;
    height: 856px;
    background: var(--label-paper);
    font-family: "EB Garamond", Georgia, serif;
  }
  .label-frame {
    position: absolute;
    inset: 24px;
    border: 2px solid var(--frame-gold);
  }
  .vineyard-art {
    position: absolute;
    left: 113px;
    top: 59px;
    width: 644px;
    height: 386px;
    background: radial-gradient(ellipse at 50% 55%, var(--art-dark) 0%, #b9b6b2 45%, var(--art-light) 75%, var(--label-paper) 100%);
  }
  .winery-name {
    position: absolute;
    left: 119px;
    top: 512px;
    font-size: 42px;
    font-weight: 600;
    letter-spacing: 0.5px;
    color: var(--ink);
    text-transform: uppercase;
    white-space: nowrap;
  }
  .label-copy {
    position: absolute;
    left: 121px;
    top: 600px;
    width: 660px;
    font-size: 21px;
    line-height: 30px;
    color: var(--body-grey);
  }
  .origin-line {
    position: absolute;
    left: 121px;
    top: 698px;
    font-size: 29px;
    font-weight: 600;
    color: var(--accent-gold);
    text-transform: uppercase;
    white-space: nowrap;
  }
</style>
</head>
<body>
  <main class="canvas">
    <section class="wine-label">
      <div class="label-frame"></div>
      <div class="vineyard-art" role="img" aria-label="Etched ink drawing of a hillside chateau above rows of vines"></div>
      <h1 class="winery-name">Harrowgate Ridge Vintners</h1>
      <p class="label-copy">Lorem ipsum dolor sit amet, consectetuer adipiscing elit, sed diam nonummy nibh euismod tincidunt ut laoreet dolore magna aliquam erat volutpat. Ut wisi enim ad minim veniam, quis nostrud exerci</p>
      <p class="origin-line">Product of Lorem Ipsum</p>
    </section>
  </main>
</body>
</html>
```